Heartnight Soiree- The Tailored Gala

This is an elegant Dinner concert event for Valentines day February 14 2020 in Vancouver WA. Live R&B band.

Join us for an Evening of live R&B music Featuring some of Oregon and Washington's talented music artists

Tickets prices: $30 concert only pp
$60 dinner and concert pp
$90 VIP Dinner & one drink/Concert/Premium Seating/Special Gift pp
Doors open @ 6:45 Event is 7:30 to 10:30
Location: Larkspur
417 Fenwick Ave.B Vancouver, WA 98664

www.teamhollowfen.com for more info.

Target Market(s)

Adults /Couples

Industry/Entity Type

Entertainment Industry

Font styles to use
Sans Serif
Decorative

Colors

Designer to choose colors to be used in the design.

Requirements
Must have
• Add the logos for Sponsors of the Event. Brindles is the main sponsor of the event.
• Main colors should be Red and right for valentine. Needs to be sized for a 5x7 Flyer
• Include the pictures of the Music Artists

```html
<!DOCTYPE html>
<html lang="en">
<head>
<meta charset="utf-8">
<title>Valentines Day Dinner Concert</title>
<link rel="stylesheet" href="https://fonts.googleapis.com/css2?family=Cinzel:wght@400&family=Permanent+Marker&family=Teko:wght@400;500;600&display=swap">
<style>
  :root {
    --backdrop: #6e3550;
    --flyer-deep: #3a0519;
    --flyer-mid: #8a0f3c;
    --pink: #f06aa8;
    --pink-soft: #f7a8cb;
    --gold: #f5cf7a;
    --white: #ffffff;
    --band: #1e0310;
    --teal: #3ab7a4;
    --heart: #c8122c;
    --heart-text: #7fb3c9;
  }
  * { margin: 0; padding: 0; box-sizing: border-box; }
  html, body { width: 1200px; height: 960px; overflow: hidden; }
  body {
    background: var(--backdrop);
    display: flex; align-items: center; justify-content: center;
    font-family: "Teko", sans-serif;
  }
  .flyer {
    position: relative;
    width: 640px; height: 896px;
    overflow: hidden;
    background:
      radial-gradient(circle at 50% 28%, rgba(216,30,104,.75), transparent 45%),
      radial-gradient(circle at 20% 70%, rgba(216,30,104,.45), transparent 35%),
      radial-gradient(circle at 85% 60%, rgba(216,30,104,.4), transparent 30%),
      linear-gradient(180deg, var(--flyer-mid) 0%, var(--flyer-deep) 40%, var(--flyer-mid) 70%, var(--flyer-deep) 100%);
    box-shadow: 0 20px 50px rgba(0,0,0,.35);
    color: var(--white);
    text-align: center;
  }
  .flyer > * { position: absolute; left: 0; right: 0; }
  .site-url {
    top: 44px; font-size: 20px; line-height: 1; letter-spacing: 4px;
    color: var(--pink-soft); font-weight: 500;
  }
  .title-script {
    top: 72px; font-family: "Permanent Marker", cursive;
    font-size: 74px; line-height: 1; font-weight: 400; color: var(--white);
    text-shadow: 0 0 18px rgba(255,120,180,.6);
  }
  .title-serif {
    top: 168px; font-family: "Cinzel", serif; font-size: 52px;
    line-height: 1; font-weight: 400; letter-spacing: 2px;
  }
  .rule { height: 3px; left: 40px; right: 40px; background: var(--pink); }
  .rule-top { top: 236px; }
  .rule-mid { top: 646px; }
  .rule-low { top: 810px; }
  .event-date {
    top: 250px; font-family: "Cinzel", serif; font-size: 38px; line-height: 1.05;
  }
  .event-city { font-size: 30px; display: block; }
  .live-band { top: 270px; left: auto; right: 14px; width: 140px; height: 130px; }
  .invite {
    top: 376px; font-size: 38px; font-weight: 600; font-style: italic;
    color: var(--gold); line-height: 1;
  }
  .featuring {
    top: 418px; font-size: 22px; font-weight: 500; line-height: 1; text-transform: uppercase;
  }
  .artist {
    left: auto; right: auto;
    width: 136px; height: 136px; border-radius: 50%;
    box-shadow: 0 0 22px rgba(255,140,200,.55);
  }
  .artist-1 { left: 22px;  top: 458px; background: radial-gradient(circle at 50% 45%, #4a3a40, #1d3f8a); }
  .artist-2 { left: 176px; top: 484px; background: radial-gradient(circle at 50% 40%, #5a4a5a, #1b1520); }
  .artist-3 { left: 330px; top: 466px; background: radial-gradient(circle at 50% 40%, #6a2a2a, #140d10); }
  .artist-4 { left: 484px; top: 496px; background: radial-gradient(circle at 50% 40%, #4a3630, #b9b9b9); }
  .prices {
    top: 656px; font-size: 24px; line-height: 1; color: var(--pink);
    font-weight: 500; text-transform: uppercase;
  }
  .doors, .location {
    font-size: 22px; line-height: 1; font-weight: 500; text-transform: uppercase;
  }
  .doors { top: 758px; }
  .location { top: 784px; }
  .sponsor-band {
    top: auto; bottom: 0; height: 76px;
    background: var(--band);
    display: flex; align-items: center; justify-content: space-around;
    padding: 0 20px;
  }
  .sponsor { font-size: 30px; font-weight: 500; line-height: 1; display: flex; align-items: center; gap: 8px; }
  .sponsor-clapwell { color: var(--teal); }
  .sponsor-brindles { color: var(--gold); }
  .sponsor-marlowe { color: var(--white); font-size: 24px; }
  .sponsor-dot { width: 22px; height: 22px; border-radius: 50%; background: var(--teal); }
</style>
</head>
<body>
  <main class="flyer">
    <div class="site-url">WWW.TEAMHOLLOWFEN.COM</div>
    <h1 class="title-script">Valentines Day</h1>
    <h2 class="title-serif">DINNER CONCERT</h2>
    <div class="rule rule-top"></div>
    <p class="event-date">FEBRUARY 14 2020<span class="event-city">VANCOUVER WA</span></p>

    <svg class="live-band" viewBox="0 0 140 130" aria-label="Live R&amp;B band heart">
      <path d="M70 124 C20 90 4 62 4 38 C4 16 22 4 40 4 C54 4 64 12 70 24 C76 12 86 4 100 4 C118 4 136 16 136 38 C136 62 120 90 70 124 Z" fill="var(--heart)"/>
      <text x="70" y="52" text-anchor="middle" font-family="Teko, sans-serif" font-size="30" font-weight="500" fill="var(--heart-text)">LIVE R&amp;B</text>
      <text x="70" y="80" text-anchor="middle" font-family="Teko, sans-serif" font-size="30" font-weight="500" fill="var(--heart-text)">BAND</text>
    </svg>

    <p class="invite">JOIN US FOR AN EVENING OF LIVE R&amp;B MUSIC</p>
    <p class="featuring">Featuring some of Oregon and Washington's talanted music artists</p>

    <div class="artist artist-1" role="img" aria-label="Portrait photo of music artist one"></div>
    <div class="artist artist-2" role="img" aria-label="Portrait photo of music artist two"></div>
    <div class="artist artist-3" role="img" aria-label="Portrait photo of music artist three"></div>
    <div class="artist artist-4" role="img" aria-label="Portrait photo of music artist four"></div>

    <div class="rule rule-mid"></div>
    <p class="prices">
      $30 concert only pp<br>
      $60 dinner and concert pp<br>
      $90 VIP dinner &amp; one drink/concert/<br>
      premium seating/special gift pp
    </p>
    <p class="doors">Doors open at 6:45 &nbsp;Event is 7:30 to 10:30</p>
    <p class="location">Location: Larkspur &nbsp;417 Fenwick Ave.B Vancouver, WA 98664</p>
    <div class="rule rule-low"></div>

    <footer class="sponsor-band">
      <span class="sponsor sponsor-clapwell"><span class="sponsor-dot"></span>CLAPWELL</span>
      <span class="sponsor sponsor-brindles">BRINDLES</span>
      <span class="sponsor sponsor-marlowe">The Marlowe Bloom Salon Spa</span>
    </footer>
  </main>
</body>
</html>
```